Business Card Design Project

Hello
I want a Simple Business card that uses the company logo that is easily reasonable but looks professional as I am an IT Services company and would look to share these cards with prospective clients.
The details are:
Kestrel Arc Solutions
14 Morrow Lane
Birmingham
B7 4QX
Telephone 0845 217 6640
I would like my name Oliver Hastings and my title Director on the card.
Target Market(s)
IT Professionals
Industry/Entity Type
Business

```html
<!DOCTYPE html>
<html lang="en">
<head>
<meta charset="utf-8">
<title>Kestrel Arc Solutions – Business Card</title>
<link rel="stylesheet" href="https://fonts.googleapis.com/css2?family=Montserrat:wght@300;700&family=Nunito+Sans:wght@400;700&display=swap">
<style>
  :root {
    --backdrop: #e9eaeb;
    --card: #ffffff;
    --ink: #231f20;
    --leaf: #8cc63f;
  }
  * { box-sizing: border-box; margin: 0; padding: 0; }
  html, body { width: 1200px; height: 1200px; overflow: hidden; }
  body {
    background: var(--backdrop);
    position: relative;
    font-family: "Nunito Sans", sans-serif;
    color: var(--ink);
  }
  .card {
    position: absolute;
    left: 174px;
    width: 851px;
    height: 486px;
    background: var(--card);
  }
  .card--front { top: 70px; }
  .card--back { top: 642px; }

  .brand {
    position: absolute;
    display: flex;
    align-items: center;
    gap: 14px;
  }
  .brand__dot {
    width: 34px;
    height: 34px;
    border-radius: 50%;
    background: var(--leaf);
    flex: none;
  }
  .brand__name {
    font-family: "Nunito Sans", sans-serif;
    font-weight: 700;
    font-size: 30px;
    color: var(--ink);
    white-space: nowrap;
  }
  .card--front .brand { left: 48px; top: 110px; }
  .card--back .brand {
    left: 50%;
    top: 50%;
    transform: translate(-50%, -50%);
  }

  .address {
    position: absolute;
    left: 47px;
    top: 268px;
    font-style: normal;
    font-size: 24px;
    line-height: 33px;
  }
  .address__company { font-weight: 700; }

  .divider {
    position: absolute;
    left: 433px;
    top: 45px;
    width: 2px;
    height: 392px;
    background: var(--ink);
  }

  .person {
    position: absolute;
    left: 475px;
    top: 196px;
    font-family: "Montserrat", sans-serif;
  }
  .person__name {
    font-weight: 300;
    font-size: 39px;
    line-height: 46px;
  }
  .person__title {
    font-weight: 700;
    font-size: 26px;
    letter-spacing: 1.5px;
    line-height: 34px;
  }
</style>
</head>
<body>
  <section class="card card--front">
    <div class="brand">
      <span class="brand__dot"></span>
      <span class="brand__name">Kestrel Arc Solutions</span>
    </div>
    <address class="address">
      <div class="address__company">Kestrel Arc Solutions</div>
      <div>14 Morrow Lane</div>
      <div>Birmingham</div>
      <div>B7 4QX</div>
      <div>0845 217 6640</div>
    </address>
    <div class="divider"></div>
    <div class="person">
      <div class="person__name">Oliver Hastings</div>
      <div class="person__title">DIRECTOR</div>
    </div>
  </section>

  <section class="card card--back">
    <div class="brand">
      <span class="brand__dot"></span>
      <span class="brand__name">Kestrel Arc Solutions</span>
    </div>
  </section>
</body>
</html>
```